Commercial Auto Insurance Application and Commercial Property Insurance Application

Hi I need a fillable application for my business to send to potential clients for Commercial Auto Insurance and Commercial Property Insurance. I have attached an example application I currently use for another line of insurance.
Commercial Auto Insurance Application
On the first page I would need the following:
- Business Name: (fill in area for text)
- Effective Date: (fill in area for text)
- How do you structure your business? (Check box for “Sole Proprietor”, “Partnership”, “Corporation”, “LLC”)
- Contact Name: (fill in area for text) / Phone Number: (fill in area for text) / Contact Email (fill in area for text)
- Mailing address: (fill in area for text)
- Garaging location: (fill in area for text)
- Owner Name: (fill in area for text)
- Description of Operations: (fill in area for text)
- How long has the operation been in business? (fill in area for text)
- How many years of experience does your management have in the truck/transportation industry? (fill in area for text)
Coverages
Liability Combined Single Limit: ($1,000,000 (checkbox) / $500,000 (checkbox / $300,000 (checkbox) / Other: (fill in area for text)
Uninsured Motorist CSL: (fill in area for text) (checkbox for “Rejected”)
Medical Payments: (fill in area for text)
Physical Damage: (fill in area for text) (checkbox for Rejected)
Liability Deducible: ($500 checkbox, $1,000 checkbox, $2,500 checkbox, $5,000 checkbox)
Physical Damage Deductible: ($500 checkbox, $1,000 checkbox, $2,500 checkbox, $5,000 checkbox)
Driving radius: (fill in area for text)
How many years have you had your own continuous commercial auto insurance coverage for the current business name? (fill in area for text)
Do any of your vehicles travel across state lines? Yes (checkbox)/ No (checkbox)
If yes, please list all states in which vehicles operate: (fill in area for text)
What is the maximum radius traveled for your customer's business?
0-25 miles (checkbox)
26-50 miles (checkbox)
51-75 miles (checkbox)
76-100 miles (checkbox)
101-150 miles (checkbox)
151-200 miles (checkbox)
201-300 miles (checkbox)
300+ miles (checkbox)
Would you like physical damage coverage for this vehicle? (should be for each vehicle listed)
On the 2nd page of the application I would need the following:
I would need to have it where people can fill in the vehicle information such as VIN:, Year:, Make:, Model:, Type of Vehicle:, Trailers:, Value:
I would also need to have it where people can fill in the drivers with their driver info including Name:, DOB:, DL #:, DL State:, Class of License:, Married: Yes/No, Number of years driving similar vehicle:
Please make it where you can fill in 20 vehicle's information and 20 driver's info.
For the 2nd Application I would need one for Property Insurance
On the Commercial Property Application I would need the following:
- Building Address: (fill in area for text)
- Building Description: (fill in area for text)
- Building Amount: $(fill in area for text)
- Business Personal Property Amount: $ (fill in area for text) (checkbox for Not Needed)
- Building Sq Ft: (fill in area for text)
- Total Area Sq Ft: (fill in area for text)
- Building Construction Type: Wood Frame (checkbox), Steel (checkbox), Fire Resistive (checkbox), Non-Combustible (checkbox), Other (fill in area for text)
- # of stories: (fill in area for text)
- Year Built: (fill in area for text)
- Wiring improvement year: (fill in area for text)
- Roofing improvement year: (fill in area for text)
- Plumbing improvement year: (fill in area for text)
- Heating improvement year: (fill in area for text)
- What is to the right of the building and distance: (fill in area for text)
- What is to the left of the building and distance: (fill in area for text)
- What is in front of the building and distance: (fill in area for text)
- What is behind the building and distance: (fill in area for text)
- Burglar alarm installation and serviced by: (fill in area for text) None (checkbox)
- Does the premises have fire protection? Sprinkler system (checkbox), Fire detection (checkbox), Other: (fill in area for text) None (checkbox)

```html
<!DOCTYPE html>
<html lang="en">
<head>
<meta charset="utf-8">
<title>Commercial Auto &amp; Commercial Property Applications</title>
<link href="https://fonts.googleapis.com/css2?family=Montserrat:wght@400;500;600;700&display=swap" rel="stylesheet">
<style>
:root{
  --bg:#1b96c6;
  --navy:#0a2a78;
  --green:#2e9e3f;
  --field:#dcdddf;
  --ink:#2a2a2a;
  --rule:#e4e5e7;
  --paper:#ffffff;
}
*{box-sizing:border-box;margin:0;padding:0}
html,body{width:1200px;height:772px;overflow:hidden;background:var(--bg)}
body{position:relative;font-family:"Montserrat",Arial,sans-serif;color:var(--ink)}
.sheet{position:absolute;top:30px;width:554px;height:716px;background:var(--paper)}
.sheet--auto{left:28px}
.sheet--property{left:611px}
.sheet::after{content:"";position:absolute;left:0;right:0;bottom:0;height:2px;background:var(--green)}
.masthead{position:absolute;left:0;top:0;right:0;height:103px;border-bottom:3px solid var(--green)}
.masthead__title{position:absolute;left:0;top:0;width:274px;height:100px;background:var(--navy);color:#fff;padding:34px 0 0 12px}
.masthead__kicker{font-size:13px;font-weight:500;letter-spacing:.2px}
.masthead__main{font-size:23px;font-weight:500;line-height:1.15;margin-top:1px}
.masthead__main em{font-style:normal;color:var(--green)}
.agency{position:absolute;right:14px;top:24px;text-align:right}
.agency__name{display:inline-flex;align-items:center;gap:6px;font-size:16px;font-weight:700;color:var(--navy);letter-spacing:.3px}
.agency__mark{width:10px;height:10px;background:var(--green)}
.agency__contact{font-size:7.6px;font-weight:500;line-height:10px;margin-top:13px;color:#111}
.row{position:absolute;left:0;right:0;display:flex;align-items:center;padding:0 12px;border-bottom:1px solid var(--rule);font-size:8.6px;white-space:nowrap}
.row--stack{flex-direction:column;align-items:stretch;justify-content:center;gap:5px}
.row--open{border-bottom:none}
.line{display:flex;align-items:center}
.lbl{flex:none}
.lbl--l{width:78px;text-align:right;margin-right:8px}
.lbl--r{width:92px;text-align:right;margin-right:8px;margin-left:auto;white-space:normal;line-height:1.25}
.field{display:block;height:20px;background:var(--field);flex:none;width:var(--w,100px);font-size:8.6px;line-height:20px;padding-left:6px}
.field--grow{flex:1;width:auto}
.field--tall{height:39px}
.opt{display:inline-flex;align-items:center;margin-right:var(--gap,12px);flex:none}
.box{width:14px;height:14px;background:var(--field);margin-right:7px;flex:none}
.band{position:absolute;left:0;right:0;height:26px;background:var(--navy);color:#fff;display:flex;align-items:center;padding-left:19px;font-size:13px;font-weight:500}
.band__mark{width:8px;height:8px;background:var(--green);margin-right:7px}
.ml{margin-left:auto}
</style>
</head>
<body>

<section class="sheet sheet--auto">
  <header class="masthead">
    <div class="masthead__title">
      <div class="masthead__kicker">Commercial Auto</div>
      <div class="masthead__main">Insurance <em>Application</em></div>
    </div>
    <div class="agency">
      <div class="agency__name"><span class="agency__mark"></span>PRAIRIEVIEW INSURANCE</div>
      <div class="agency__contact">4820 Maple Ridge Ave Suite 310, Fairview CA 90210<br>(555) 014-2290<br>www.prairieviewinsurance.com</div>
    </div>
  </header>

  <div class="row" style="top:103px;height:35px">
    <span class="lbl lbl--l">Business Name:</span><span class="field" style="--w:175px"></span>
    <span class="lbl lbl--r">Effective Date:</span><span class="field" style="--w:175px"></span>
  </div>
  <div class="row" style="top:138px;height:26px">
    <span class="lbl" style="margin-right:9px">How do you structure your business?</span>
    <span class="opt"><span class="box"></span>Sole Proprietor</span>
    <span class="opt"><span class="box"></span>Partnership</span>
    <span class="opt"><span class="box"></span>Corporation</span>
    <span class="opt"><span class="box"></span>LLC</span>
  </div>
  <div class="row" style="top:164px;height:30px">
    <span class="lbl lbl--l">Contact Name:</span><span class="field" style="--w:175px"></span>
    <span class="lbl lbl--r">Phone Number:</span><span class="field" style="--w:175px"></span>
  </div>
  <div class="row" style="top:194px;height:28px">
    <span class="lbl lbl--l">Mailing address:</span><span class="field" style="--w:175px"></span>
    <span class="lbl lbl--r">Garaging location:</span><span class="field" style="--w:175px"></span>
  </div>
  <div class="row" style="top:222px;height:29px">
    <span class="lbl lbl--l">Owner Name:</span><span class="field" style="--w:175px"></span>
    <span class="lbl lbl--r">Description of Operations:</span><span class="field" style="--w:175px"></span>
  </div>
  <div class="row" style="top:251px;height:28px">
    <span class="lbl" style="margin-right:10px">How long has the operation been in business?</span><span class="field field--grow"></span>
  </div>
  <div class="row" style="top:279px;height:33px">
    <span class="lbl" style="margin-right:7px">How many years of experience does your management have in the truck/transportation industry?</span><span class="field field--grow"></span>
  </div>

  <div class="band" style="top:312px"><span class="band__mark"></span>Coverages</div>

  <div class="row" style="top:338px;height:34px">
    <span class="lbl" style="margin-right:8px">Liability Combined Single Limit:</span>
    <span class="opt"><span class="box"></span>$1,000,000</span>
    <span class="opt"><span class="box"></span>$500,000</span>
    <span class="opt"><span class="box"></span>$300,000</span>
    <span class="lbl ml" style="margin-right:9px">Other:</span><span class="field" style="--w:103px"></span>
  </div>
  <div class="row" style="top:372px;height:30px">
    <span class="lbl" style="margin-right:10px">Uninsured Motorist CSL:</span><span class="field field--grow"></span>
    <span class="opt" style="margin-left:13px;margin-right:0"><span class="box"></span>Rejected</span>
  </div>
  <div class="row" style="top:402px;height:31px">
    <span class="lbl" style="margin-right:9px">Medical Payments:</span><span class="field" style="--w:117px"></span>
    <span class="lbl" style="margin:0 9px 0 14px">Physical Damage:</span><span class="field field--grow"></span>
    <span class="opt" style="margin-left:13px;margin-right:0"><span class="box"></span>Rejected</span>
  </div>
  <div class="row" style="top:433px;height:24px;--gap:17px">
    <span class="lbl" style="width:138px">Liability Deductible:</span>
    <span class="opt"><span class="box"></span>$500</span>
    <span class="opt"><span class="box"></span>$1,000</span>
    <span class="opt"><span class="box"></span>$2,500</span>
    <span class="opt"><span class="box"></span>$5,000</span>
  </div>
  <div class="row" style="top:457px;height:24px;--gap:17px">
    <span class="lbl" style="width:138px">Physical Damage Deductible:</span>
    <span class="opt"><span class="box"></span>$500</span>
    <span class="opt"><span class="box"></span>$1,000</span>
    <span class="opt"><span class="box"></span>$2,500</span>
    <span class="opt"><span class="box"></span>$5,000</span>
  </div>
  <div class="row" style="top:481px;height:30px">
    <span class="lbl" style="margin-right:8px">Driving radius:</span><span class="field field--grow"></span>
  </div>
  <div class="row row--stack" style="top:511px;height:44px">
    <span class="lbl">How many years have you had your own continuous commercial auto insurance coverage for the current business name?</span>
    <span class="field" style="--w:100%"></span>
  </div>
  <div class="row" style="top:555px;height:24px;--gap:45px">
    <span class="lbl" style="margin-right:9px">Do any of your vehicles travel across state lines?</span>
    <span class="opt"><span class="box"></span>Yes</span>
    <span class="opt"><span class="box"></span>No</span>
  </div>
  <div class="row" style="top:579px;height:30px">
    <span class="lbl" style="margin-right:7px">If yes, please list all states in which vehicles operate:</span><span class="field field--grow"></span>
  </div>
  <div class="row row--stack" style="top:609px;height:41px;gap:4px">
    <div class="line">
      <span class="lbl" style="margin-right:8px">What is the maximum radius traveled for your customer's business?</span>
      <span class="opt"><span class="box"></span>0-25 miles</span>
      <span class="opt"><span class="box"></span>26-50 miles</span>
      <span class="opt" style="margin-right:0"><span class="box"></span>51-75 miles</span>
    </div>
    <div class="line" style="--gap:14px">
      <span class="opt"><span class="box"></span>76-100 miles</span>
      <span class="opt"><span class="box"></span>101-150 miles</span>
      <span class="opt"><span class="box"></span>151-200 miles</span>
      <span class="opt"><span class="box"></span>201-300 miles</span>
      <span class="opt"><span class="box"></span>300+ miles</span>
    </div>
  </div>
  <div class="row row--stack row--open" style="top:650px;height:62px;gap:4px">
    <span class="lbl">Would you like physical damage coverage for this vehicle? (should be for each vehicle listed)</span>
    <span class="field field--tall" style="--w:100%"></span>
  </div>
</section>

<section class="sheet sheet--property">
  <header class="masthead">
    <div class="masthead__title">
      <div class="masthead__kicker">Commercial Property</div>
      <div class="masthead__main"><em>Application</em></div>
    </div>
    <div class="agency">
      <div class="agency__name"><span class="agency__mark"></span>PRAIRIEVIEW INSURANCE</div>
      <div class="agency__contact">4820 Maple Ridge Ave Suite 310, Fairview CA 90210<br>(555) 014-2290<br>www.prairieviewinsurance.com</div>
    </div>
  </header>

  <div class="row" style="top:103px;height:37px">
    <span class="lbl" style="width:83px">Business Name:</span><span class="field" style="--w:360px"></span>
  </div>
  <div class="row" style="top:140px;height:30px">
    <span class="lbl" style="width:83px">Building Address:</span><span class="field" style="--w:360px"></span>
  </div>
  <div class="row" style="top:170px;height:31px">
    <span class="lbl" style="margin-right:8px">Building Description:</span><span class="field" style="--w:207px"></span>
    <span class="lbl" style="margin:0 9px 0 8px">Building Amount:</span><span class="field field--grow">$</span>
  </div>
  <div class="row" style="top:201px;height:32px">
    <span class="lbl" style="margin-right:7px">Business Personal Property Amount:</span><span class="field" style="--w:141px">$</span>
    <span class="opt" style="margin-left:10px"><span class="box"></span>Not Needed</span>
  </div>
  <div class="row" style="top:233px;height:32px">
    <span class="lbl" style="margin-right:10px">Building Sq Ft:</span><span class="field" style="--w:175px"></span>
    <span class="lbl ml" style="margin-right:11px">Total Area Sq Ft:</span><span class="field" style="--w:175px"></span>
  </div>
  <div class="row" style="top:265px;height:29px;--gap:14px">
    <span class="lbl" style="margin-right:7px">Building Construction Type:</span>
    <span class="opt"><span class="box"></span>Wood Frame</span>
    <span class="opt"><span class="box"></span>Steel</span>
    <span class="opt"><span class="box"></span>Fire Resistive</span>
    <span class="opt"><span class="box"></span>Non-Combustible</span>
  </div>
  <div class="row" style="top:294px;height:39px">
    <span class="lbl" style="margin-right:9px">Other:</span><span class="field" style="--w:152px"></span>
    <span class="lbl" style="margin:0 10px">&#35; of stories:</span><span class="field" style="--w:154px"></span>
    <span class="lbl" style="margin:0 7px 0 10px">Year Built:</span><span class="field field--grow"></span>
  </div>
  <div class="row" style="top:333px;height:34px">
    <span class="lbl" style="margin-right:4px">Wiring improvement year:</span><span class="field" style="--w:46px"></span>
    <span class="lbl" style="margin:0 6px">Roofing improvement year:</span><span class="field" style="--w:55px"></span>
    <span class="lbl" style="margin:0 4px 0 7px">Roofing improvement year:</span><span class="field field--grow"></span>
  </div>
  <div class="row" style="top:367px;height:33px">
    <span class="lbl" style="margin-right:12px">Plumbing improvement year:</span><span class="field" style="--w:53px"></span>
    <span class="lbl" style="margin:0 12px">Heating improvement year:</span><span class="field" style="--w:54px"></span>
  </div>
  <div class="row" style="top:400px;height:34px">
    <span class="lbl" style="width:222px">What is to the right of the building and distance:</span><span class="field field--grow"></span>
  </div>
  <div class="row" style="top:434px;height:34px">
    <span class="lbl" style="width:222px">What is to the left of the building and distance:</span><span class="field field--grow"></span>
  </div>
  <div class="row" style="top:468px;height:33px">
    <span class="lbl" style="width:222px">What is in front of the building and distance:</span><span class="field field--grow"></span>
  </div>
  <div class="row" style="top:501px;height:34px">
    <span class="lbl" style="width:222px">What is behind the building and distance:</span><span class="field field--grow"></span>
  </div>
  <div class="row row--stack" style="top:535px;height:56px;gap:8px">
    <div class="line"><span class="lbl" style="width:222px">Burglar alarm installation and serviced by:</span><span class="field field--grow"></span></div>
    <div class="line" style="padding-left:222px"><span class="opt"><span class="box"></span>None</span></div>
  </div>
  <div class="row row--stack row--open" style="top:591px;height:120px;justify-content:flex-start;padding-top:8px;gap:9px">
    <div class="line">
      <span class="lbl" style="width:222px">Does the premises have fire protection?</span>
      <span class="opt"><span class="box"></span>Sprinkler system</span>
      <span class="opt"><span class="box"></span>Fire detection</span>
    </div>
    <div class="line">
      <span class="lbl" style="width:222px;text-align:right;padding-right:15px">Other:</span><span class="field field--grow"></span>
    </div>
    <div class="line" style="padding-left:222px"><span class="opt"><span class="box"></span>None</span></div>
  </div>
</section>

</body>
</html>
```